Before the kettle cools, pocast with content in its majority of technology

Page dedicated to a pocast with content in its majority of technology. The page also contains the chapters of the podcast (pluggin tunebrim) will also contain news. Preferably Worpress. There is already a very basic page with a simple theme, the logo and little more, I would like something more professional. Www.cuandoelfarosebalancea.com The logo does not want to change.

Target Market(s)

Anyone

Colors

Requirements
Must have
• You can put the tunebrim pluggin with the podcast chapters

```html
<!DOCTYPE html>
<html lang="es">
<head>
<meta charset="utf-8">
<title>Before the kettle cools</title>
<link href="https://fonts.googleapis.com/css2?family=Montserrat:wght@400;600;700&family=Open+Sans:wght@400;600&display=swap" rel="stylesheet">
<style>
:root{
  --orange:#f26b1d;
  --dark:#1f1f1f;
  --darker:#151515;
  --text:#555;
  --muted:#999;
  --light:#f1f1f1;
  --line:#e2e2e2;
  --white:#fff;
}
*{margin:0;padding:0;box-sizing:border-box}
html,body{width:1200px;height:2676px;overflow:hidden;background:var(--white);font-family:"Open Sans",sans-serif;color:var(--text)}
.topbar{height:60px;background:var(--darker);display:flex;align-items:center;justify-content:space-between;padding:0 60px}
.socials{display:flex;gap:14px}
.socials span{width:14px;height:14px;border-radius:50%;background:#bbb;display:block}
.search{width:150px;height:26px;border-bottom:1px solid #666;color:#888;font-size:12px;display:flex;align-items:center;justify-content:space-between}
.logo{position:absolute;left:540px;top:8px;width:120px;height:100px;display:flex;flex-direction:column;align-items:center;justify-content:center;gap:6px}
.logo .mark{width:44px;height:44px;border-radius:50%;background:var(--orange)}
.logo .name{font-family:"Montserrat",sans-serif;font-weight:700;font-size:11px;color:var(--orange);text-align:center;line-height:1.2;text-transform:uppercase}
.nav{height:60px;background:var(--dark);display:flex;align-items:center;justify-content:center;gap:40px;font-family:"Montserrat",sans-serif;font-size:12px;font-weight:600;color:var(--white)}
.nav .gap{width:120px}
.hero{position:relative;height:520px;background:linear-gradient(135deg,#3a3a3a,#8a8a8a 45%,#c86a3a 75%,#2a2a2a);display:flex;flex-direction:column;align-items:center;justify-content:center;gap:30px;padding-top:80px}
.hero h1{font-family:"Montserrat",sans-serif;font-weight:700;font-size:52px;color:var(--white);letter-spacing:3px;text-transform:uppercase}
.btn{background:var(--orange);color:var(--white);font-family:"Montserrat",sans-serif;font-weight:700;font-size:13px;padding:16px 34px;border-radius:30px;text-transform:uppercase}
.dots{position:absolute;bottom:20px;display:flex;gap:8px}
.dots span{width:8px;height:8px;border-radius:50%;background:rgba(255,255,255,.5)}
.dots span:first-child{background:var(--white)}
.section-icon{width:34px;height:34px;margin:0 auto 14px;border-radius:50%;border:3px solid var(--orange)}
.section-title{font-family:"Montserrat",sans-serif;font-weight:700;font-size:24px;color:#333;text-align:center;text-transform:uppercase}
.rule{width:60px;height:3px;background:var(--orange);margin:12px auto 0}
.welcome{padding:60px 80px 80px;text-align:center;font-size:12px;line-height:1.8}
.welcome .hi{color:var(--orange);font-weight:600;margin-top:24px}
.welcome .lead{font-weight:700;color:#333;font-size:15px;margin:30px 0 24px}
.prices{display:flex;gap:30px;justify-content:center}
.price{width:240px;border:1px solid var(--line)}
.price .head{height:60px;background:var(--light);display:flex;align-items:center;justify-content:center;gap:10px;font-family:"Montserrat",sans-serif;font-weight:700;color:var(--orange);font-size:16px}
.price .head b{width:30px;height:30px;border-radius:50%;background:var(--orange);color:var(--white);display:flex;align-items:center;justify-content:center;font-size:13px}
.price .cost{height:64px;display:flex;align-items:center;justify-content:center;gap:8px;font-size:18px;font-weight:600;color:#333}
.price .cost s{font-size:12px;color:var(--muted)}
.price .deal{height:50px;background:var(--light);display:flex;align-items:center;justify-content:center;color:var(--orange);font-weight:600;font-size:14px}
.welcome .after{margin-top:34px}
.podcasts{background:var(--light);height:1218px;padding:60px 90px 0}
.grid{display:grid;grid-template-columns:1fr 1fr;gap:50px 40px;margin-top:40px}
.player{height:160px;background:var(--white);border:1px solid var(--line);display:flex;padding:14px}
.player .main{flex:1;display:flex;flex-direction:column;justify-content:space-between;padding-right:14px}
.player .row{display:flex;justify-content:space-between;align-items:center;font-size:12px;color:#333}
.player .brand{font-family:"Open Sans",sans-serif;font-weight:600;font-size:11px;color:#333}
.player .play{width:36px;height:36px;border-radius:50%;background:var(--orange);display:flex;align-items:center;justify-content:center}
.player .wave{flex:1;height:40px;background:linear-gradient(#ddd,#c8c8c8);margin-left:12px}
.player .time{font-size:10px;color:var(--muted)}
.art{width:130px;height:130px;background:#2c2c2c}
.card h3{font-family:"Montserrat",sans-serif;font-weight:600;font-size:16px;color:var(--orange);margin:16px 0 8px}
.card p{font-size:12px;line-height:1.8}
.more{display:flex;justify-content:center;margin-top:380px}
.footer{height:98px;background:var(--darker);display:flex;align-items:center;justify-content:space-between;padding:0 60px;color:#888;font-size:11px}
</style>
</head>
<body>
<header>
  <div class="topbar">
    <div class="socials"><span></span><span></span><span></span><span></span><span></span><span></span></div>
    <div class="search">Search... <svg width="12" height="12" viewBox="0 0 12 12"><circle cx="5" cy="5" r="4" fill="none" stroke="#888" stroke-width="1.5"/><line x1="8" y1="8" x2="11" y2="11" stroke="#888" stroke-width="1.5"/></svg></div>
  </div>
  <div class="logo"><span class="mark"></span><span class="name">Before the kettle cools</span></div>
  <nav class="nav"><span>HOME</span><span>ABOUT US</span><span>PODCASTS</span><span class="gap"></span><span>BLOG</span><span>REVIEWS</span><span>CONTACT US</span></nav>
</header>

<section class="hero" role="img" aria-label="Studio microphone photograph with warm stage lights">
  <h1>Before the kettle cools</h1>
  <span class="btn">Listen Podcast</span>
  <div class="dots"><span></span><span></span><span></span><span></span></div>
</section>

<section class="welcome">
  <div class="section-icon"></div>
  <h2 class="section-title">Welcome to our website</h2>
  <div class="rule"></div>
  <p class="hi">Hola a todos!</p>
  <p>Hoy quiero presentaros un proyecto nacido de las ganas de hablar de tecnología, de series y de todo lo que nos rodea cada día.<br>Cada semana publicamos un nuevo capítulo con noticias, opiniones y pruebas de los dispositivos que más nos interesan.</p>
  <p>El catálogo es muy amplio, actual y completo. Puedes escucharnos desde cualquier dispositivo y en cualquier momento, y si te gusta,<br>puedes apoyarnos con una suscripción para seguir creciendo y mejorando cada capítulo.</p>
  <p class="lead">Estos son los precios:</p>
  <div class="prices">
    <div class="price"><div class="head"><b>1</b>Meses</div><div class="cost">6 €</div><div class="deal">Base</div></div>
    <div class="price"><div class="head"><b>3</b>Meses</div><div class="cost">16 € <s>18 €</s></div><div class="deal">Descuento de 11%</div></div>
    <div class="price"><div class="head"><b>6</b>Meses</div><div class="cost">28 € <s>36 €</s></div><div class="deal">Descuento de 22%</div></div>
    <div class="price"><div class="head"><b>12</b>Meses</div><div class="cost">48 € <s>72 €</s></div><div class="deal">Descuento de 33%</div></div>
  </div>
  <p class="after">Si te animas, con una única suscripción tendrás acceso a todos los capítulos anteriores y a los que están por llegar.<br>Puedes escucharnos en el móvil, en el ordenador o en tu televisor, sin anuncios y con la mejor calidad de sonido.<br>Es gratis probarlo y sencillo.<br>Nos escuchamos en el siguiente.</p>
</section>

<section class="podcasts">
  <div class="section-icon"></div>
  <h2 class="section-title">Our podcasts</h2>
  <div class="rule"></div>
  <div class="grid">
    <article class="card">
      <div class="player"><div class="main"><div class="row"><span>Un anuncio y una prueba</span><span class="brand">tunebrim</span></div><div class="row"><span class="play"><svg width="12" height="14"><polygon points="0,0 12,7 0,14" fill="#fff"/></svg></span><span class="wave"></span></div><div class="time">© 2017 · 00:00</div></div><div class="art" role="img" aria-label="Episode cover artwork"></div></div>
      <h3>Un anuncio y una prueba</h3>
      <p>Si, lo sé, no suelo hacer anuncios, pero esta vez merece la pena. Os cuento cómo ha sido la prueba de este mes, qué nos ha gustado y qué no, y por qué creemos que os puede interesar.</p>
    </article>
    <article class="card">
      <div class="player"><div class="main"><div class="row"><span>Seguridad en tu Mail</span><span class="brand">tunebrim</span></div><div class="row"><span class="play"><svg width="12" height="14"><polygon points="0,0 12,7 0,14" fill="#fff"/></svg></span><span class="wave"></span></div><div class="time">© 2017 · 00:00</div></div><div class="art" role="img" aria-label="Episode cover artwork in blue tones" style="background:#3b4f9a"></div></div>
      <h3>Seguridad en tu Mail</h3>
      <p>Hoy quiero hablar de la seguridad en el correo electrónico, de los riesgos más comunes y de algunos consejos sencillos que podéis aplicar hoy mismo.</p>
    </article>
    <article class="card">
      <div class="player"><div class="main"><div class="row"><span>Kestrelo KePad2, calidad precio</span><span class="brand">tunebrim</span></div><div class="row"><span class="play"><svg width="12" height="14"><polygon points="0,0 12,7 0,14" fill="#fff"/></svg></span><span class="wave"></span></div><div class="time">© 2017 · 00:00</div></div><div class="art" role="img" aria-label="Episode cover artwork in orange" style="background:var(--orange)"></div></div>
      <h3>Kestrelo KePad2, calidad precio insuperable</h3>
      <p>Si, lo sé, no suelo hacer análisis, pero esta tableta me ha sorprendido. Os cuento mis impresiones después de varias semanas de uso diario.</p>
    </article>
    <article class="card">
      <div class="player"><div class="main"><div class="row"><span>Notaverde, sin lugar a dudas</span><span class="brand">tunebrim</span></div><div class="row"><span class="play"><svg width="12" height="14"><polygon points="0,0 12,7 0,14" fill="#fff"/></svg></span><span class="wave"></span></div><div class="time">© 2017 · 00:00</div></div><div class="art" role="img" aria-label="Episode cover artwork in green" style="background:#4aa84a"></div></div>
      <h3>Notaverde, sin lugar a dudas</h3>
      <p>En este podcast os hablo de la aplicación de notas que uso a diario, cómo la organizo, sus mejores trucos y por qué la recomiendo.</p>
    </article>
  </div>
  <div class="more"><span class="btn">View all podcast</span></div>
</section>

<footer class="footer">
  <span>Copyright © 2017 Tetera Media. All Right Reserved</span>
  <div class="socials"><span></span><span></span><span></span><span></span><span></span><span></span></div>
</footer>
</body>
</html>
```